Bold Website Redesign for a Disruptive Training Brand

Brightmoor Labs is a bold, no-fluff sales & leadership training company powered by AI-driven practice and behavioral science. We’ve already built our website structure and copy in Craftly.io — now we need a designer to fully transform the visual design across all pages (Home, Approach, Programs, About, Contact).
We’re looking for a modern, memorable, high-performance aesthetic that blends human energy, science, and tech without feeling corporate or safe. Clean, bold typography, fluid layout, strong emotional hero moments, subtle motion, and imagery that mixes real people with abstract scientific/tech visuals.Because our clients are primarily North American, please ensure any human photography or AI-generated imagery reflects a North American business context and demographics (modern, diverse, and realistic).

Your job is visual redesign only — no coding required.
The final design must be practical to rebuild inside Craftly.io.

A full, detailed creative brief (plus logo files) is included in the uploaded files.
If you can bring a mix of edge, intelligence, and strong visual storytelling, we’d love to see your work.

Website is already built in Craftly.io at - https://brightmoor-website-tempdesign.craftly.app — structure is set, visuals need redesign.

```html
<!DOCTYPE html>
<html lang="en">
<head>
<meta charset="utf-8">
<title>Brightmoor Labs — Training That Practices Back</title>
<link href="https://fonts.googleapis.com/css2?family=Montserrat:wght@800;900&family=Poppins:wght@400;500;600&display=swap" rel="stylesheet">
<style>
:root{
  --navy:#0b1838;
  --navy-deep:#081230;
  --blue:#3d68b8;
  --blue-mid:#2f58a8;
  --sky:#45b4e4;
  --ink:#1d2433;
  --muted:#5b6374;
  --pale:#eef2f9;
  --line:#d9e0ec;
  --white:#ffffff;
}
*{box-sizing:border-box;margin:0;padding:0}
html,body{width:1200px;height:4121px;overflow:hidden}
body{font-family:"Poppins",sans-serif;color:var(--ink);background:var(--white);position:relative}
.abs{position:absolute}
section,.footer{position:absolute;left:0;width:1200px}
a{color:inherit;text-decoration:none}

/* hero */
.hero{top:0;height:568px;background:radial-gradient(ellipse at 40% 60%,#173a86 0%,var(--navy) 55%,var(--navy-deep) 100%);overflow:hidden}
.hero-visual{left:470px;top:80px;width:730px;height:440px;background:radial-gradient(ellipse at 45% 45%,#2c7de0 0%,#1a4fb0 35%,#0d2460 70%,transparent 100%);opacity:.9}
.hero-wave{left:0;bottom:0}
.logo{display:flex;align-items:center;gap:10px;color:var(--white);font-weight:600;font-size:17px;letter-spacing:.5px}
.logo-mark{width:18px;height:18px;background:var(--white)}
.nav{left:521px;top:38px;display:flex;color:var(--white);font-size:13px}
.nav a{margin-right:42px}
.btn-talk{left:966px;top:27px;width:92px;height:40px;background:var(--sky);color:var(--white);font-size:13px;display:flex;align-items:center;justify-content:center}
.hero-title{left:141px;top:166px;font-family:"Montserrat",sans-serif;font-weight:900;font-size:35px;line-height:39px;color:var(--white);text-transform:uppercase}
.hero-sub{left:141px;top:249px;width:360px;font-size:16.5px;line-height:24px;color:var(--white)}
.hero-copy{left:141px;top:307px;width:370px;font-size:12.5px;line-height:19px;color:var(--white)}
.btn-hero{top:389px;height:37px;font-size:12px;color:var(--white);display:flex;align-items:center;justify-content:center;gap:6px}
.btn-primary{left:141px;width:152px;background:var(--sky)}
.btn-outline{left:302px;width:112px;border:1.5px solid var(--white)}

/* headings */
.h2{width:1200px;left:0;text-align:center;font-size:29px;font-weight:400;color:var(--ink)}
.h2 b{font-weight:600;color:var(--blue)}
.rule{left:568px;width:64px;height:2px;background:var(--blue)}
.lead{width:1200px;left:0;text-align:center;font-size:13px;color:var(--ink)}

.problem-title{top:648px;font-size:34px;line-height:49px}
.problem-copy{left:190px;width:820px;top:797px;text-align:center;font-size:14.5px;line-height:25px;color:var(--muted)}
.pill{left:398px;top:886px;width:402px;height:44px;border:1.5px solid var(--blue);border-radius:22px;color:var(--blue);font-size:13.5px;display:flex;align-items:center;justify-content:center}

.story-img{left:0;top:1040px;width:578px;height:421px;border-radius:0 12px 12px 0;background:linear-gradient(120deg,#c7d2e3 0%,#7b93b8 40%,#2c3f66 75%,#1b2742 100%)}
.story-title{left:621px;top:1094px;width:460px;font-size:30px;line-height:45px;font-weight:400}
.story-title b{font-weight:600;color:var(--blue)}
.story-copy{left:621px;top:1222px;width:430px;font-size:13px;line-height:24px;color:var(--ink)}
.btn-round{left:621px;top:1363px;width:176px;height:45px;border-radius:23px;background:var(--blue);color:var(--white);font-size:14px;display:flex;align-items:center;justify-content:center}

/* pillars */
.pillars{top:1540px;height:570px}
.pillar{top:255px;width:280px}
.pillar .icon{width:70px;height:70px;border-radius:50%;background:var(--blue);display:flex;align-items:center;justify-content:center;box-shadow:0 6px 14px rgba(61,104,184,.3)}
.pillar .icon.alt{background:var(--sky)}
.pillar h3{margin-top:48px;font-size:22px;font-weight:400}
.pillar p{margin-top:14px;font-size:12.5px;line-height:24px;color:var(--ink);width:240px}
.divider{top:255px;width:1px;height:221px;background:var(--line)}

/* programs */
.card{top:2350px;width:440px;height:482px;border:1px solid var(--line);border-radius:8px;background:var(--white);box-shadow:0 4px 16px rgba(20,40,90,.06);overflow:hidden;text-align:center}
.card .c-icon{margin:42px auto 0;width:86px;height:86px;border-radius:50%;background:var(--pale);display:flex;align-items:center;justify-content:center}
.card h3{margin-top:24px;font-size:17.5px;font-weight:600}
.card .c-sub{margin-top:8px;font-size:14px}
.card .c-rule{margin:20px auto 0;width:56px;height:2px;background:var(--blue)}
.card .c-body{margin:22px auto 0;width:360px;font-size:12.5px;line-height:24px;color:var(--muted)}
.checks{margin:26px 0 0 26px;display:grid;grid-template-columns:226px 190px;row-gap:20px;text-align:left;font-size:12.5px}
.checks span{display:flex;align-items:center;gap:8px}
.card-foot{position:absolute;left:0;bottom:0;width:100%;height:48px;background:var(--pale);display:flex;align-items:center;justify-content:center;font-size:14px}

/* contact */
.contact{top:2900px;height:700px}
.contact-bg{left:0;top:0}
.field{height:53px;background:var(--white);border-radius:3px;display:flex;align-items:center;font-size:12.5px;color:#6b7280}
.field .fi{width:52px;display:flex;justify-content:center;border-right:1px solid var(--line);height:22px;align-items:center;margin-right:12px}
.field.tall{height:109px;align-items:flex-start;padding-top:16px}
.submit{left:291px;top:503px;width:616px;height:53px;border-radius:27px;background:var(--sky);color:var(--white);font-size:13px;font-weight:600;display:flex;align-items:center;justify-content:center;letter-spacing:.3px}

/* footer */
.footer{top:3584px;height:537px;background:var(--navy-deep);color:var(--white)}
.cta-title{left:141px;top:57px;width:560px;font-size:30px;line-height:45px;font-weight:400}
.btn-cta{left:850px;top:77px;width:208px;height:45px;border-radius:23px;background:var(--blue-mid);font-size:14px;display:flex;align-items:center;justify-content:center}
.f-rule{left:141px;top:202px;width:917px;height:1px;background:rgba(255,255,255,.2)}
.f-about{left:141px;top:352px;width:220px;font-size:13px;line-height:20px}
.follow{left:141px;top:432px;display:flex;align-items:center;gap:10px;font-size:12.5px}
.soc{width:24px;height:24px;border-radius:50%;border:1.5px solid var(--white)}
.soc.fill{background:var(--sky);border-color:var(--sky)}
.f-col h4{font-size:15px;font-weight:500;margin-bottom:18px}
.f-col li{list-style:none;font-size:13px;line-height:29px}
.c-row{display:flex;align-items:center;gap:14px;font-size:13px;line-height:22px;margin-bottom:22px}
.c-ic{width:30px;height:30px;border-radius:50%;background:rgba(255,255,255,.12);display:flex;align-items:center;justify-content:center;flex:none}
.c-ic.on{background:var(--blue-mid)}
.copyright{left:0;bottom:0;width:1200px;height:38px;background:#050c22;text-align:center;font-size:11px;line-height:38px;color:rgba(255,255,255,.75)}
</style>
</head>
<body>

<section class="hero">
  <div class="abs hero-visual" role="img" aria-label="Glowing blue tech cubes with icons for ideas, people, targets, growth and sales training"></div>
  <a class="abs logo" style="left:141px;top:34px"><span class="logo-mark"></span>Brightmoor Labs</a>
  <nav class="abs nav"><a>Home</a><a>Approach</a><a>Programs</a><a>About</a><a>Contact</a></nav>
  <a class="abs btn-talk">Let's Talk</a>
  <h1 class="abs hero-title">Training That<br>Practices Back.</h1>
  <p class="abs hero-sub">AI-driven sustainment that builds mastery – so you don't have to.</p>
  <p class="abs hero-copy">You'll see measurable growth as your people turn insight into habit — automatically, sustainably, and without extra work for their leaders.</p>
  <a class="abs btn-hero btn-primary">See How We Do It →</a>
  <a class="abs btn-hero btn-outline">Let's Talk →</a>
  <svg class="abs hero-wave" width="1200" height="120" viewBox="0 0 1200 120">
    <path d="M0 120 L0 100 C300 80 700 70 1200 0 L1200 120 Z" fill="#4fc0ec"/>
    <path d="M0 120 L0 104 C350 92 760 80 1200 62 L1200 120 Z" fill="#ffffff"/>
  </svg>
</section>

<h2 class="abs h2 problem-title">The Real Problem Isn't Your People — <b>It's The<br>Forgetting Curve.</b></h2>
<div class="abs rule" style="top:765px"></div>
<p class="abs problem-copy">Within a week, most training disappears. Leaders are left guessing who's using what they learned — and no one has time to fix it. We built Brightmoor Labs to make progress automatic, measurable, and real.</p>
<a class="abs pill">Watch how sustained practice changes the curve</a>

<div class="abs story-img" role="img" aria-label="Business person touching a rising growth graph with analytics icons"></div>
<h2 class="abs story-title">Built By People Who've <b>Led The Change Themselves.</b></h2>
<p class="abs story-copy">Behind Brightmoor Labs are leaders who've lived the challenge of making learning last. They've scaled companies, built cultures, and led transformation — and now they've designed the system they always wished existed.</p>
<a class="abs btn-round">Meet the Team</a>

<section class="pillars">
  <svg class="abs" style="left:0;top:0" width="1200" height="570" viewBox="0 0 1200 570">
    <path d="M0 20 C150 -10 300 40 480 20 C650 0 800 -10 1000 15 C1100 28 1160 20 1200 10 L1200 540 C1050 560 900 530 720 548 C520 568 300 530 150 548 C80 556 30 560 0 555 Z" fill="#eef2f9"/>
  </svg>
  <h2 class="abs h2" style="top:126px">Practice Made <b>Permanent.</b></h2>
  <div class="abs rule" style="top:178px"></div>
  <p class="abs lead" style="top:205px">You'll replace "hope they remember" with a system that makes sure they do.</p>

  <div class="abs pillar" style="left:141px">
    <div class="icon"><svg width="34" height="34" viewBox="0 0 24 24" fill="none" stroke="#fff" stroke-width="1.4"><path d="M9 4a4 4 0 0 0-4 4 3 3 0 0 0 0 6 4 4 0 0 0 4 4h1V4z"/><path d="M15 4a4 4 0 0 1 4 4 3 3 0 0 1 0 6 4 4 0 0 1-4 4h-1V4z"/></svg></div>
    <h3>Learn</h3>
    <p>Fast, focused workshops, built on science, that install the mindset and skills that matter most.</p>
  </div>
  <div class="abs divider" style="left:453px"></div>
  <div class="abs pillar" style="left:491px">
    <div class="icon alt"><svg width="34" height="34" viewBox="0 0 24 24" fill="none" stroke="#fff" stroke-width="1.5"><circle cx="12" cy="12" r="8"/><path d="M8 12l3 3 5-6"/></svg></div>
    <h3>Certify</h3>
    <p>Programmatic AI-driven practice and feedback - mastery without management overhead.</p>
  </div>
  <div class="abs divider" style="left:794px"></div>
  <div class="abs pillar" style="left:832px">
    <div class="icon"><svg width="34" height="34" viewBox="0 0 24 24" fill="none" stroke="#fff" stroke-width="1.4"><circle cx="12" cy="12" r="8"/><path d="M8 15c2-5 6-6 8-7-1 4-3 7-8 7z"/></svg></div>
    <h3>Sustain</h3>
    <p>Light-touch challenges and dashboards that keep skills sharp long after training ends.</p>
  </div>
</section>

<h2 class="abs h2" style="top:2220px">Practice Made <b>Permanent.</b></h2>
<div class="abs rule" style="top:2273px"></div>
<p class="abs lead" style="top:2299px">You'll replace "hope they remember" with a system that makes sure they do.</p>

<article class="abs card" style="left:141px">
  <div class="c-icon"><svg width="44" height="44" viewBox="0 0 24 24" fill="none" stroke="#3d68b8" stroke-width="1.2"><path d="M4 20h16"/><path d="M7 17v-4M11 17V9M15 17v-6M19 17V6"/><path d="M5 11l5-4 4 3 6-5"/></svg></div>
  <h3>Adaptive Sales Mastery</h3>
  <p class="c-sub">Transform capability into consistent revenue growth</p>
  <div class="c-rule"></div>
  <p class="c-body">Turn your sales team into a consistent, confident growth engine — one that practices, improves, and performs without you chasing follow-through.</p>
  <div class="checks">
    <span><svg width="14" height="14" viewBox="0 0 24 24" fill="none" stroke="#2da84a" stroke-width="3"><path d="M4 12l5 5L20 6"/></svg>Science-Based Frameworks</span>
    <span><svg width="14" height="14" viewBox="0 0 24 24" fill="none" stroke="#2da84a" stroke-width="3"><path d="M4 12l5 5L20 6"/></svg>AI-Assisted Practice</span>
    <span><svg width="14" height="14" viewBox="0 0 24 24" fill="none" stroke="#2da84a" stroke-width="3"><path d="M4 12l5 5L20 6"/></svg>Coaching Feedback Loops</span>
    <span><svg width="14" height="14" viewBox="0 0 24 24" fill="none" stroke="#2da84a" stroke-width="3"><path d="M4 12l5 5L20 6"/></svg>Progress Dashboards</span>
  </div>
  <div class="card-foot">Talk with us about Leadership Mastery</div>
</article>

<article class="abs card" style="left:618px">
  <div class="c-icon"><svg width="44" height="44" viewBox="0 0 24 24" fill="none" stroke="#3d68b8" stroke-width="1.2"><circle cx="12" cy="8" r="2.5"/><circle cx="6" cy="10" r="2"/><circle cx="18" cy="10" r="2"/><path d="M7.5 17a4.5 4.5 0 0 1 9 0M2.5 17a3.5 3.5 0 0 1 5-3M21.5 17a3.5 3.5 0 0 0-5-3"/></svg></div>
  <h3>Leadership Mastery</h3>
  <p class="c-sub">Build leaders who create lasting impact</p>
  <div class="c-rule"></div>
  <p class="c-body">Develop leaders who create clarity, coach for growth, and drive results that last — even amid real-world complexity.</p>
  <div class="checks" style="margin-left:44px;grid-template-columns:204px 180px">
    <span><svg width="14" height="14" viewBox="0 0 24 24" fill="none" stroke="#2da84a" stroke-width="3"><path d="M4 12l5 5L20 6"/></svg>Decision Mastery</span>
    <span><svg width="14" height="14" viewBox="0 0 24 24" fill="none" stroke="#2da84a" stroke-width="3"><path d="M4 12l5 5L20 6"/></svg>Sustained Practice</span>
    <span><svg width="14" height="14" viewBox="0 0 24 24" fill="none" stroke="#2da84a" stroke-width="3"><path d="M4 12l5 5L20 6"/></svg>Coaching Skills</span>
    <span><svg width="14" height="14" viewBox="0 0 24 24" fill="none" stroke="#2da84a" stroke-width="3"><path d="M4 12l5 5L20 6"/></svg>Change Leadership</span>
  </div>
  <div class="card-foot">Talk with us about Leadership Mastery</div>
</article>

<section class="contact">
  <svg class="abs contact-bg" width="1200" height="700" viewBox="0 0 1200 700" role="img" aria-label="Blue-tinted photo of people working at laptops">
    <defs><linearGradient id="cbg" x1="0" y1="0" x2="1" y2="1"><stop offset="0" stop-color="#3a63b4"/><stop offset="1" stop-color="#2b4f9c"/></linearGradient></defs>
    <path d="M0 40 C200 10 380 50 600 30 C820 10 1000 50 1200 25 L1200 700 L0 700 Z" fill="url(#cbg)"/>
    <path d="M0 680 C250 640 500 670 700 650 C900 630 1080 670 1200 655 L1200 700 L0 700 Z" fill="#081230"/>
  </svg>
  <h2 class="abs h2" style="top:130px;color:#fff;font-size:32px">Contact Information</h2>
  <p class="abs lead" style="top:184px;color:#fff">Reach out through any of these channels, and we'll respond quickly to start the conversation.</p>
  <div class="abs field" style="left:291px;top:236px;width:301px"><span class="fi"><svg width="14" height="14" viewBox="0 0 24 24" fill="none" stroke="#9aa3b2" stroke-width="1.6"><circle cx="12" cy="8" r="4"/><path d="M4 21a8 8 0 0 1 16 0"/></svg></span>First Name</div>
  <div class="abs field" style="left:607px;top:236px;width:300px"><span class="fi"><svg width="14" height="14" viewBox="0 0 24 24" fill="none" stroke="#9aa3b2" stroke-width="1.6"><circle cx="12" cy="8" r="4"/><path d="M4 21a8 8 0 0 1 16 0"/></svg></span>Last Name</div>
  <div class="abs field" style="left:291px;top:303px;width:301px"><span class="fi"><svg width="14" height="14" viewBox="0 0 24 24" fill="none" stroke="#9aa3b2" stroke-width="1.6"><rect x="3" y="5" width="18" height="14" rx="2"/><path d="M3 7l9 6 9-6"/></svg></span>Your Email</div>
  <div class="abs field" style="left:607px;top:303px;width:300px"><span class="fi"><svg width="14" height="14" viewBox="0 0 24 24" fill="none" stroke="#9aa3b2" stroke-width="1.6"><path d="M5 3h4l2 5-3 2a11 11 0 0 0 6 6l2-3 5 2v4a2 2 0 0 1-2 2A17 17 0 0 1 3 5a2 2 0 0 1 2-2z"/></svg></span>Phone</div>
  <div class="abs field tall" style="left:291px;top:370px;width:616px"><span class="fi"><svg width="14" height="14" viewBox="0 0 24 24" fill="none" stroke="#9aa3b2" stroke-width="1.6"><circle cx="12" cy="12" r="9"/></svg></span>Your Message</div>
  <a class="abs submit">SUBMIT NOW</a>
</section>

<footer class="footer">
  <h2 class="abs cta-title">Ready To See What Lasting Capability Looks Like?</h2>
  <a class="abs btn-cta">Start a Conversation</a>
  <div class="abs f-rule"></div>

  <a class="abs logo" style="left:141px;top:290px"><span class="logo-mark"></span>Brightmoor Labs</a>
  <p class="abs f-about">Making learning that sticks through AI-driven sustainment and behavioral science.</p>
  <div class="abs follow">Follow Us:<span class="soc"></span><span class="soc fill"></span><span class="soc"></span></div>

  <div class="abs f-col" style="left:422px;top:265px"><h4>Quick Links</h4><ul><li>Home</li><li>Approach</li><li>Programs</li><li>About</li><li>Contact</li></ul></div>
  <div class="abs f-col" style="left:592px;top:265px"><h4>Other Links</h4><ul><li>Adaptive Sales Mastery</li><li>Leadership Mastery</li><li>Terms &amp; Conditions</li><li>Privacy Policy</li></ul></div>
  <div class="abs f-col" style="left:819px;top:265px;width:260px">
    <h4>Contact Us</h4>
    <div class="c-row"><span class="c-ic"><svg width="14" height="14" viewBox="0 0 24 24" fill="none" stroke="#fff" stroke-width="2"><path d="M12 22s7-7 7-12a7 7 0 0 0-14 0c0 5 7 12 7 12z"/><circle cx="12" cy="10" r="2.5"/></svg></span>4820 N Larkspur Ave Suite<br>210 Fairview, AZ 85099</div>
    <div class="c-row"><span class="c-ic on"><svg width="14" height="14" viewBox="0 0 24 24" fill="#fff"><path d="M5 3h4l2 5-3 2a11 11 0 0 0 6 6l2-3 5 2v4a2 2 0 0 1-2 2A17 17 0 0 1 3 5a2 2 0 0 1 2-2z"/></svg></span>Phone: +1 (555) 014-2290</div>
    <div class="c-row"><span class="c-ic"><svg width="14" height="14" viewBox="0 0 24 24" fill="#fff"><path d="M3 6h18v12H3z"/><path d="M3 6l9 7 9-7" stroke="#081230" stroke-width="1.6" fill="none"/></svg></span>contact@brightmoorlabs.com</div>
  </div>

  <div class="abs copyright">© 2024 Brightmoor Labs. All Rights Reserved.</div>
</footer>

</body>
</html>
```